Brim Contractors

We are a group of people that doing a picking fruits like Oranges and grapes seasonal. We would like to have the colors " light black or black " back ground of the card. Thanks

Industry/Entity Type

Group

Contact Information for Business Card

Mob 0498213564 . Fax 03 5187 3940. P.O.Box 517 Tarrawong Vic 3461

```html
<!DOCTYPE html>
<html lang="en">
<head>
<meta charset="utf-8">
<title>Brim Contractors – Business Card</title>
<link rel="stylesheet" href="https://fonts.googleapis.com/css2?family=Open+Sans:wght@400&display=swap">
<style>
  :root {
    --stage: #3a3a3a;
    --card: #231f20;
    --green: #8cc63f;
    --orange: #d98a1f;
    --purple: #5b2a86;
    --ink: #e9e9e9;
  }
  * { margin: 0; padding: 0; box-sizing: border-box; }
  html, body { width: 1200px; height: 900px; overflow: hidden; }
  body {
    background: var(--stage);
    font-family: "Open Sans", Arial, sans-serif;
    position: relative;
  }
  .card {
    position: absolute;
    width: 560px;
    height: 320px;
    background: var(--card);
    border-radius: 2px;
    box-shadow: 0 10px 28px rgba(0,0,0,.45);
  }
  .card--front { left: 120px; top: 80px; }
  .card--back  { left: 400px; top: 450px; }

  .brand {
    display: flex;
    align-items: center;
    gap: 10px;
    color: var(--green);
    font-weight: 400;
    white-space: nowrap;
  }
  .brand__dot {
    width: 14px; height: 14px;
    border-radius: 50%;
    background: var(--orange);
  }
  .card--front .brand {
    position: absolute;
    left: 0; right: 0; top: 132px;
    justify-content: center;
    font-size: 34px;
  }
  .card--back .brand {
    position: absolute;
    left: 42px; top: 40px;
    font-size: 22px;
  }
  .services {
    position: absolute;
    left: 42px; top: 130px;
    color: var(--green);
    font-size: 19px;
  }
  .contact {
    position: absolute;
    left: 42px; top: 180px;
    list-style: none;
    font-size: 12.5px;
    line-height: 1.55;
    color: var(--ink);
  }
  .contact__label { color: var(--green); }
  .tagline {
    position: absolute;
    right: 40px; bottom: 64px;
    color: var(--orange);
    font-size: 19px;
  }
  .lockup {
    position: absolute;
    right: 40px; bottom: 50px;
    font-size: 36px;
  }
</style>
</head>
<body>
  <section class="card card--front">
    <div class="brand"><span class="brand__dot"></span>Brim Contractors</div>
  </section>

  <section class="card card--back">
    <div class="brand"><span class="brand__dot"></span>Brim Contractors</div>
    <p class="services">Citrus - Grapes</p>
    <ul class="contact">
      <li><span class="contact__label">Mobile:</span> 0498213564</li>
      <li><span class="contact__label">Fax:</span> 03 5187 3940</li>
      <li><span class="contact__label">P.O.</span>Box 517 Tarrawong Vic 3461</li>
    </ul>
    <p class="tagline">Fruits Picking</p>
  </section>

  <div class="brand lockup"><span class="brand__dot"></span>Brim Contractors</div>
</body>
</html>
```